| Pairlocket | ||
| "Lanternmade Insurance" (this tagline includes the mathmatic "squared" symbol-see logo #161 winner) | ||
| Use fonts in logo. However, we may provide other direction on fonts for Address/Phone Numbers, etc. | ||
Cutting-Edge Modern Bright & Fun-filled |
| Dana R. Whitlock, MBA | ||
| Agency Principal | ||
| To Be Determined | ||
| TBD | ||
| dana@trypairlocket.com | ||
| www.trypairlocket.com | ||
1. We will need business cards for 2 people, Dana Whitlock (info provided above) and Morgan Whitlock...info as follows: Morgan P. Whitlock, MBA Agency Principal morgan@trypairlocket.com cell: 555.204.7316 2. Designer has provided final files to Mark Studio Hive. #161 was selected as Winner. This design has multiple components, please note. 3. Our logo style and design is somewhat "Retro" and cool, hip. We are in the insurance industry but definitely want to achieve a different "non-standard" look and feel. 4. Read Logo Brief for more information about the style of the two (twin brothers) Agency Principals. |
We are thinking that the "bottle cap" portion of our logo along with the "Pairlocket" portion would look good on the back of the business card. The bottle cap portion taking up most of the back of the card. Would like various options for the back. |
Download project material |
| pairlocket_17707.pdf |
| 1_17708.ai |
| Oak_Cellar_Depot_Business_Card_1_17709.jpg Pairlocket - Bus Card - example card design. We would like to see a style similar to this. |
| Brisk_Kettle_Business_Card_Example_17710.jpg Pairlocket - Bus Card - example card design. We would like to see a style similar to this. |

```html
<!DOCTYPE html>
<html lang="en">
<head>
<meta charset="utf-8">
<title>Pairlocket Business Card</title>
<link href="https://fonts.googleapis.com/css2?family=Open+Sans:wght@400;600;700&display=swap" rel="stylesheet">
<style>
  :root {
    --bg: #e9e4dc;
    --card-white: #ffffff;
    --brand-blue: #1f5f94;
    --brand-green: #4f9a3a;
    --text-grey: #6b6b6b;
    --icon-grey: #8a8a8a;
  }
  * { margin: 0; padding: 0; box-sizing: border-box; }
  html, body { width: 1200px; height: 541px; overflow: hidden; }
  body {
    background: var(--bg);
    font-family: "Open Sans", Arial, sans-serif;
    position: relative;
  }
  .card {
    position: absolute;
    box-shadow: 0 6px 18px rgba(0,0,0,0.25);
    overflow: hidden;
  }
  .card-front { left: 77px; top: 149px; width: 504px; height: 343px; background: var(--card-white); }
  .card-back { left: 600px; top: 168px; width: 497px; height: 348px; background: var(--brand-blue); }

  .brand {
    position: absolute;
    left: 26px;
    top: 118px;
    width: 250px;
  }
  .brand-row { display: flex; align-items: center; gap: 8px; }
  .brand-dot {
    width: 24px; height: 24px; border-radius: 50%;
    background: var(--brand-green);
    flex: none;
  }
  .brand-name {
    font-weight: 700;
    font-size: 32px;
    line-height: 1;
    color: var(--brand-blue);
    letter-spacing: -0.5px;
  }
  .brand-tagline {
    margin-top: 4px;
    margin-left: 34px;
    font-size: 7.5px;
    font-weight: 600;
    letter-spacing: 1.2px;
    color: var(--brand-blue);
    text-transform: uppercase;
  }

  .contacts {
    position: absolute;
    left: 288px;
    top: 96px;
    list-style: none;
  }
  .contacts li {
    display: flex;
    align-items: center;
    gap: 8px;
    font-size: 11.5px;
    color: var(--text-grey);
    height: 20px;
  }
  .contacts svg { width: 10px; height: 10px; fill: var(--icon-grey); flex: none; }

  .band {
    position: absolute;
    top: 223px;
    height: 72px;
    color: #fff;
    padding: 14px 14px;
    font-size: 12px;
    line-height: 1.55;
  }
  .band-person { left: 0; width: 259px; background: var(--brand-green); }
  .band-address { left: 265px; right: 0; background: var(--brand-blue); }
  .person-name { font-size: 15px; font-weight: 600; }
  .person-name small { font-size: 10px; font-weight: 400; }

  .back-mark {
    position: absolute;
    left: 0; right: 0; top: 62px;
    display: flex; justify-content: center; align-items: center; gap: 10px;
  }
  .back-mark .brand-dot { background: #ffffff; width: 30px; height: 30px; }
  .back-mark .brand-name { color: #ffffff; font-size: 34px; }
  .back-url {
    position: absolute;
    left: 0; right: 0; top: 188px;
    text-align: center;
    color: #ffffff;
    font-size: 12.5px;
  }
</style>
</head>
<body>
  <section class="card card-front">
    <div class="brand">
      <div class="brand-row">
        <span class="brand-dot"></span>
        <span class="brand-name">Pairlocket</span>
      </div>
      <div class="brand-tagline">Lanternmade Insurance</div>
    </div>

    <ul class="contacts">
      <li><svg viewBox="0 0 10 10"><path d="M2 0h2l1 3-1.5 1a6 6 0 0 0 2.5 2.5L7 5l3 1v2c0 1-1 2-2 2A8 8 0 0 1 0 2c0-1 1-2 2-2z"/></svg>000.000.0000</li>
      <li><svg viewBox="0 0 10 10"><rect x="2.5" y="0" width="5" height="10" rx="1"/></svg>555.417.8820</li>
      <li><svg viewBox="0 0 10 10"><rect x="1" y="3" width="8" height="6"/><rect x="2.5" y="0" width="5" height="3"/></svg>000.000.0000</li>
      <li><svg viewBox="0 0 10 10"><path d="M0 2h10v6H0z"/></svg>dana@trypairlocket.com</li>
      <li><svg viewBox="0 0 10 10"><circle cx="5" cy="5" r="5"/></svg>www.trypairlocket.com</li>
    </ul>

    <div class="band band-person">
      <div class="person-name">Dana R. Whitlock, <small>MBA</small></div>
      <div>Agency Principal</div>
    </div>
    <div class="band band-address">
      <div>Post box 0000</div>
      <div>city abc road country</div>
    </div>
  </section>

  <section class="card card-back">
    <div class="back-mark">
      <span class="brand-dot"></span>
      <span class="brand-name">Pairlocket</span>
    </div>
    <div class="back-url">www.trypairlocket.com</div>
  </section>
</body>
</html>
```